Vetrune
@PEmmo, #128 looks good. Could I see some designs for other stationeries? Thanks
@Lumetra - #130 looks good thanks. I think we need phone number on the letterhead.
Thank you all for the inputs - these are great designs.
@Quorby, for #127, I dont think we need phone and email on the envelope. We can leave the web address. thanks.
@Lumetra - i like the idea of #96. But i dont like the black back. I like an orange back as shown #87. Also, the contact info should probably be left aligned with the logo on top.
Thanks for the inputs. I am not a fan of the color black.
@Dorvel, Could you please make the logo bigger in #91?
Dear Ju,
Pls see private message from the top right of the page..
Thanks..
Thanks for the inputs Quorby. I like #64. Would we see a variety in the font color?
Please, please - do not post pre-made templates or templates that were used in a previous contest. It does nothing but kill your credibility.

```html
<!DOCTYPE html>
<html lang="en">
<head>
<meta charset="utf-8">
<title>Vetrune business card</title>
<link href="https://fonts.googleapis.com/css2?family=Arimo:wght@400;700&display=swap" rel="stylesheet">
<style>
  :root {
    --backdrop: #e9e6e2;
    --card-white: #ffffff;
    --card-grey: #e4e4e4;
    --ink: #1a1a1a;
    --ink-soft: #555555;
    --orange: #f39a1c;
    --orange-deep: #ef6a12;
    --red: #d61f1f;
    --yellow: #f8c21a;
    --brand-green: #5fb531;
  }
  * { margin: 0; padding: 0; box-sizing: border-box; }
  html, body { width: 1200px; height: 550px; overflow: hidden; }
  body {
    background: var(--backdrop);
    font-family: "Arimo", Arial, sans-serif;
    position: relative;
  }
  .card {
    position: absolute;
    top: 80px;
    width: 528px;
    height: 390px;
    border-radius: 14px;
    overflow: hidden;
    box-shadow: 0 6px 18px rgba(0,0,0,0.25);
  }
  .card-front {
    left: 36px;
    background: linear-gradient(160deg, var(--card-white) 0%, #f7f7f7 55%, var(--card-grey) 100%);
  }
  .card-back {
    left: 636px;
    background: linear-gradient(100deg, var(--yellow) 0%, var(--orange) 35%, var(--orange-deep) 65%, var(--red) 100%);
  }

  /* front */
  .holder {
    position: absolute;
    right: 50px;
    top: 32px;
    text-align: right;
  }
  .holder-name { font-weight: 700; font-size: 17px; color: var(--ink); }
  .holder-title { font-size: 11px; color: var(--ink-soft); margin-top: 4px; }
  .accent-square {
    position: absolute;
    right: 22px;
    top: 24px;
    width: 22px;
    height: 30px;
    background: linear-gradient(180deg, var(--orange), var(--red));
  }
  .brand {
    position: absolute;
    left: 44px;
    top: 128px;
    display: flex;
    align-items: center;
    gap: 14px;
  }
  .brand-dot {
    width: 84px;
    height: 84px;
    border-radius: 50%;
    background: var(--brand-green);
  }
  .brand-name {
    font-weight: 700;
    font-size: 66px;
    color: var(--ink);
    line-height: 1;
  }
  .tagline {
    position: absolute;
    left: 142px;
    top: 208px;
    font-size: 9px;
    color: var(--ink-soft);
    letter-spacing: 0.3px;
  }
  .contact {
    position: absolute;
    left: 296px;
    top: 306px;
    display: flex;
    font-size: 10px;
    color: var(--ink);
  }
  .contact-lines { padding-right: 14px; border-right: 1px solid #9a9a9a; }
  .contact-lines p, .address p { line-height: 19px; white-space: nowrap; }
  .contact-lines b { color: var(--orange-deep); font-weight: 700; margin-right: 4px; }
  .address { padding-left: 10px; }

  /* back */
  .back-glow {
    position: absolute;
    left: 40px;
    top: 30px;
    width: 300px;
    height: 300px;
    border-radius: 50%;
    background: rgba(255,255,255,0.12);
  }
  .back-brand {
    position: absolute;
    right: 40px;
    top: 214px;
    display: flex;
    align-items: center;
    gap: 8px;
  }
  .back-brand .brand-dot { width: 44px; height: 44px; background: rgba(255,255,255,0.9); }
  .back-brand .brand-name { font-size: 22px; color: #ffffff; }
  .back-web {
    position: absolute;
    right: 40px;
    top: 290px;
    font-size: 12px;
    color: #ffffff;
  }
</style>
</head>
<body>
  <section class="card card-front">
    <div class="accent-square"></div>
    <div class="holder">
      <p class="holder-name">Kemi Adeyoro</p>
      <p class="holder-title">President &amp; CEO</p>
    </div>
    <div class="brand">
      <div class="brand-dot"></div>
      <span class="brand-name">Vetrune</span>
    </div>
    <p class="tagline">IT SOLUTIONS TAILORED FOR YOUR BUSINESS</p>
    <div class="contact">
      <div class="contact-lines">
        <p><b>P:</b>410.555.0143</p>
        <p><b>E:</b>kemi@vetrune.com</p>
        <p><b>W:</b>www.vetrune.com</p>
      </div>
      <div class="address">
        <p>4417 Brellin Way</p>
        <p>Ostwick</p>
        <p>MD 20491</p>
      </div>
    </div>
  </section>

  <section class="card card-back">
    <div class="back-glow"></div>
    <div class="back-brand">
      <div class="brand-dot"></div>
      <span class="brand-name">Vetrune</span>
    </div>
    <p class="back-web">www.vetrune.com</p>
  </section>
</body>
</html>
```